Greatest Mom Greeting Card

A 5in x 7in greeting card design for a company that sells political humor greeting cards online. The specifications are as follows:

Front Text: "You’re the best mom. The greatest mom. The most beautiful mom. VERY SUCCESSFUL." in scripty font for everything but the portion in all caps. All caps type should be in a bold san serif condensed font.

Front Art: Think flowers and light pastels.

Inner Right Text: "Happy Mother’s Day. THE HAPPIEST." same script font for Happy Mother's Day, and same bold san-serif font for The Happiest.

Inner Right Art: Include graphic/illustration of Harold Brennick with thumbs up.

```html
<!DOCTYPE html>
<html lang="en">
<head>
<meta charset="utf-8">
<title>Greatest Mom Greeting Card</title>
<link rel="stylesheet" href="https://fonts.googleapis.com/css2?family=Anton&family=Yellowtail&display=swap">
<style>
  :root {
    --stage: #000000;
    --card-paper: #fdf3f6;
    --card-wash: #f8d9e3;
    --wash-warm: #fbeee6;
    --script-pink: #e3187b;
    --heart-pink: #f4b5c9;
    --ink: #141414;
    --art-tint: #f9dbe8;
  }
  * { margin: 0; padding: 0; box-sizing: border-box; }
  html, body {
    width: 1200px;
    height: 786px;
    overflow: hidden;
    background: var(--stage);
  }
  .canvas {
    position: relative;
    width: 1200px;
    height: 786px;
    background: var(--stage);
  }
  .card {
    position: absolute;
    top: 99px;
    width: 414px;
    height: 580px;
    background:
      radial-gradient(ellipse at 30% 20%, var(--card-wash) 0%, transparent 55%),
      radial-gradient(ellipse at 70% 75%, var(--wash-warm) 0%, transparent 60%),
      radial-gradient(ellipse at 15% 85%, var(--card-wash) 0%, transparent 45%),
      var(--card-paper);
    text-align: center;
    overflow: hidden;
  }
  .card--front { left: 142px; }
  .card--inside { left: 639px; }

  .hearts {
    position: absolute;
    top: 0;
    left: 0;
    width: 100%;
    height: 120px;
    background: radial-gradient(ellipse at 50% 40%, var(--heart-pink) 0%, rgba(244,181,201,0.35) 40%, transparent 75%);
    opacity: 0.55;
  }

  .script {
    font-family: "Yellowtail", cursive;
    color: var(--script-pink);
    font-weight: 400;
  }
  .headline {
    font-family: "Anton", "Oswald", sans-serif;
    color: var(--ink);
    text-transform: uppercase;
    letter-spacing: 0.5px;
  }

  .praise {
    position: absolute;
    top: 108px;
    left: 0;
    width: 100%;
  }
  .praise__line {
    display: block;
    font-size: 34px;
    line-height: 72px;
  }
  .praise__line em {
    font-style: normal;
    font-size: 50px;
  }
  .praise__closer {
    position: absolute;
    top: 337px;
    left: 0;
    width: 100%;
    font-size: 56px;
    line-height: 56px;
  }

  .greeting {
    position: absolute;
    top: 52px;
    left: 0;
    width: 100%;
    font-size: 60px;
    line-height: 58px;
  }
  .greeting__closer {
    position: absolute;
    top: 236px;
    left: 0;
    width: 100%;
    font-size: 50px;
    line-height: 56px;
  }
  .portrait {
    position: absolute;
    left: 27px;
    top: 303px;
    width: 352px;
    height: 242px;
    background: radial-gradient(ellipse at 55% 45%, var(--art-tint) 0%, rgba(249,219,232,0.4) 60%, transparent 90%);
  }
</style>
</head>
<body>
<main class="canvas">
  <section class="card card--front" aria-label="Card front">
    <div class="hearts" role="img" aria-label="Soft pink watercolor hearts"></div>
    <p class="praise script">
      <span class="praise__line">You’re the <em>best</em> mom</span>
      <span class="praise__line">The <em>greatest</em> mom</span>
      <span class="praise__line">The most <em>beautiful</em> mom</span>
    </p>
    <p class="praise__closer headline">Very<br>Successful!</p>
  </section>

  <section class="card card--inside" aria-label="Card inside right">
    <div class="hearts" role="img" aria-label="Soft pink watercolor hearts"></div>
    <h1 class="greeting script">Happy<br>Mother’s Day</h1>
    <p class="greeting__closer headline">The Happiest!</p>
    <div class="portrait" role="img" aria-label="Pink line drawing of Harold Brennick in a suit giving a thumbs up"></div>
  </section>
</main>
</body>
</html>
```